The KEP Groote Eylandt - Menu 2020

I am looking for a new desgin on our menu. Preferbly 1 page but happy for it to be in A3. See attached what we are currently using which was designed by one of our admin people which is ok but is a bit busy. The KEP logo is already in use so this would need to stay as is, otherwise the layout /design /background im happy to review all. This is a beach side pub with simple fresh food.

Target Market(s)

FIFO Workforce as well as young familes residential.

Requirements
Must have
• match the logo.
Nice to have
• on 1 page (not turn over)
Should not have
• Anything not family friendly

```html
<!DOCTYPE html>
<html lang="en">
<head>
<meta charset="utf-8">
<title>The KEP – All Day Bar Menu</title>
<link href="https://fonts.googleapis.com/css2?family=Open+Sans:wght@700&family=Roboto+Condensed:wght@400;700&family=Nanum+Pen+Script&display=swap" rel="stylesheet">
<style>
  :root{
    --blue:#1ba3dc;
    --orange:#f39a4b;
    --yellow:#f9c233;
    --ink:#232323;
    --stage:#e4e4e4;
    --paper:#ffffff;
  }
  *{box-sizing:border-box;margin:0;padding:0}
  html,body{width:1191px;height:1200px;overflow:hidden;background:var(--stage)}
  .menu{
    position:absolute;left:200px;top:42px;width:791px;height:1115px;
    background:var(--paper);border:8px solid var(--blue);
    font-family:"Roboto Condensed","Arial Narrow",sans-serif;color:var(--ink);
    font-size:11.5px;line-height:15px;overflow:hidden;
  }
  .brand{position:absolute;left:0;right:0;top:26px;text-align:center}
  .brand-name{font-family:"Roboto Condensed","Arial Narrow",sans-serif;font-weight:700;
    font-size:30px;line-height:36px;color:var(--ink);letter-spacing:.5px}

  .column{position:absolute;top:102px}
  .column-left{left:40px;width:322px}
  .column-right{left:394px;width:332px}
  .section-title{font-family:"Open Sans",Arial,sans-serif;font-weight:700;font-size:19.5px;color:var(--blue);line-height:24px;letter-spacing:.3px}
  .note{font-family:"Nanum Pen Script",cursive;font-size:15px;line-height:18px;margin:6px 0 7px}
  .item{margin-bottom:7px}
  .item-name{font-weight:700;text-transform:uppercase;font-size:11px}
  .line{display:flex;align-items:baseline}
  .line .fill{flex:1;border-bottom:1.5px dotted var(--ink);margin:0 2px;transform:translateY(-3px)}
  .line .gap{flex:1}
  .accent{color:var(--blue)}
  .sub-title{text-align:center;text-transform:uppercase;font-size:14px;margin:10px 0 4px;letter-spacing:.3px}
  .centered-note{text-align:center;margin:12px 0 22px}

  .divider{position:absolute;left:26px;right:26px;top:758px;border-top:1px solid var(--blue)}
  .fillings{position:absolute;left:43px;top:800px;width:330px;z-index:2}
  .fillings-title{text-transform:uppercase;font-size:15px;margin-left:23px;margin-bottom:8px;letter-spacing:.2px}
  .fillings-list{list-style:none;color:var(--blue);font-size:12.5px;line-height:19.5px}
  .fillings-list .line .fill{border-color:var(--blue)}
  .fillings-extra{margin-top:10px}

  .scene{position:absolute;left:0;top:780px;width:775px;height:327px}
</style>
</head>
<body>
<main class="menu">
  <header class="brand">
    <div class="brand-name">The KEP</div>
  </header>

  <section class="column column-left">
    <h2 class="section-title">ALL DAY BAR MENU</h2>
    <p class="note">Available 11:30am – 8:30pm</p>

    <div class="item">
      <div class="item-name">Crispy Chicken Wings</div>
      <div>Your Choice of Sauce (Ranch, Spicy Buffalo, BBQ or</div>
      <div class="line">South West Sauce)<span class="fill"></span>5 Wings.... $7.5</div>
      <div class="line"><span class="fill"></span>10 Wings.. $15.0</div>
    </div>
    <div class="item">
      <div class="item-name">Trio of Sliders</div>
      <div>Smoky Pulled Pork, South West Pulled Beef Brisket and</div>
      <div>Southern Fried Chicken with Sriracha Mayo</div>
      <div class="line">all served with Fresh Slaw<span class="fill"></span>$12.0</div>
    </div>
    <div class="item">
      <div class="item-name">Vege Fries</div>
      <div>Parsnip, Beets &amp; Carrot Fries with Rosemary Sea Salt</div>
      <div class="line">and Chipotle Mayo<span class="fill"></span>(V)$8.0</div>
    </div>
    <div class="item">
      <div class="item-name">Crispy Fries</div>
      <div class="line">Plain Fries<span class="fill"></span>$6.0</div>
      <div class="line">With Gravy, Shaved Gouda Cheese &amp; Grilled Bacon<span class="fill"></span>$9.0</div>
    </div>
    <div class="item line"><span class="item-name">Garlic Bread</span><span class="fill"></span>$4.0</div>
    <div class="item line"><span class="item-name">Cheesy Garlic Bread</span><span class="fill"></span>$5.0</div>

    <h3 class="sub-title">Tacos, Nachos or Quesadillas</h3>
    <div class="item">
      <div class="item-name">Tacos</div>
      <div>Soft Tortilla <span class="accent">with Your Choice of Filling</span></div>
      <div class="line">Fresh Slaw, Avocado, Sriracha Cream &amp; Lime Wedge<span class="fill"></span>$16.0</div>
    </div>
    <div class="item">
      <div class="item-name">Nachos</div>
      <div>Toasted Corn Chips Topped <span class="accent">with Your Choice of Filling</span></div>
      <div>Avocado, Fresh Tomato Salsa, Melted Cheese, Sour Cream</div>
      <div class="line">&amp; Jalapenos<span class="fill"></span>$18.0</div>
    </div>
    <div class="item">
      <div class="item-name">Quesadillas</div>
      <div>Toasted Tortilla <span class="accent">with Your Choice of Filling</span></div>
      <div>Baby Spinach, Roasted Red Pepper, Gouda</div>
      <div class="line">&amp; Buffalo Mozzarella<span class="gap"></span>$16.0</div>
    </div>
  </section>

  <section class="column column-right">
    <h2 class="section-title">BURGERS AND SALADS</h2>
    <p class="note">All burgers served with steak chips</p>

    <div class="item">
      <div class="item-name">Pulled Pork Burger</div>
      <div>Pulled Pork, Fresh Slaw, Pickles, &amp; Spicy BBQ Sauce</div>
      <div class="line">On A Brioche Bun<span class="fill"></span>$22.0</div>
    </div>
    <div class="item">
      <div class="item-name">Beef, Bacon &amp; Cheese Burger</div>
      <div>Beef Patty, Maple Bacon, Cheddar Cheese, Tomato,</div>
      <div>Cos Lettuce, Caramelised Onion</div>
      <div class="line">&amp; Smoky BBQ Sauce On A Seeded Hamburger Bun<span class="fill"></span>$22.0</div>
    </div>
    <div class="item">
      <div class="item-name">Southern Fried Chicken Burger (*Grilled Chicken Available)</div>
      <div>Chicken Breast, Sliced Havarti, Baby Spinach</div>
      <div class="line">&amp; Sriracha Mayo On A Brioche Bun<span class="fill"></span>$22.0</div>
    </div>
    <div class="item">
      <div class="item-name">South West Brisket Roll</div>
      <div>Pulled Smokey BBQ Beef Brisket with South West Sauce &amp;</div>
      <div class="line">Fresh Slaw on A Crusty Sourdough Roll<span class="fill"></span>$22.0</div>
    </div>

    <p class="centered-note">*Ask for Vegetarian Substitutes &amp;<br>All Options Can Be Served Bunless</p>

    <div class="item">
      <div class="item-name">Caesar Salad</div>
      <div>Cos Lettuce, Crispy Garlic Croutons, Bacon,</div>
      <div>Shaved Parmesan, Free Range Egg, Caesar Dressing</div>
      <div class="line">&amp; Anchovies<span class="fill"></span>$18.0</div>
    </div>
    <div class="item">
      <div class="line">Add Grilled Chicken<span class="fill"></span>$4.0</div>
      <div class="line">Add Grilled Prawns<span class="fill"></span>$8.0</div>
    </div>
    <div class="item">
      <div class="item-name">Leaf Eater Salad</div>
      <div>Baby Spinach, Mixed Green Leaves, Avocado, Roasted Red</div>
      <div>Peppers, Buffalo Mozzarella, Baked Tortilla Strips Served</div>
      <div class="line">with A Balsamic Reduction<span class="fill"></span>$16.0</div>
    </div>
    <div class="item">
      <div class="line">Add Grilled Chicken<span class="fill"></span>$4.0</div>
      <div class="line">Add Grilled Prawns<span class="fill"></span>$8.0</div>
    </div>
  </section>

  <div class="divider"></div>

  <svg class="scene" viewBox="0 0 775 327" role="img" aria-label="Beach illustration: orange palm trees against a yellow setting sun, line-drawn onion, mushroom and tomato icons, and a row of orange waves above striped bands">
    <defs>
      <linearGradient id="sunset" x1="0" y1="0" x2="0" y2="1">
        <stop offset="0" stop-color="#ffffff"/>
        <stop offset=".35" stop-color="#f8b46c"/>
        <stop offset="1" stop-color="#f9c233"/>
      </linearGradient>
    </defs>
    <rect x="420" y="0" width="355" height="190" fill="url(#sunset)"/>
    <rect x="0" y="176" width="775" height="50" fill="var(--orange)"/>
    <rect x="0" y="235" width="775" height="7" fill="var(--orange)"/>
    <rect x="0" y="250" width="775" height="17" fill="var(--yellow)"/>
    <rect x="0" y="276" width="775" height="36" fill="var(--blue)"/>
  </svg>

  <section class="fillings">
    <h3 class="fillings-title">Choose your filling from the below:</h3>
    <ul class="fillings-list">
      <li>Smokey BBQ Pulled Pork</li>
      <li>Southern Fried Chicken</li>
      <li>South West Pulled Beef Brisket</li>
      <li>Chilli Black Bean</li>
      <li class="fillings-extra line">Grilled Cajun Prawns<span class="fill"></span>$6.0</li>
    </ul>
  </section>
</main>
</body>
</html>
```